Saffron Lantern Court Business Card

I am looking for a business card desgined for my restaurant. It is an Indian restaurant, we are looking for something thats modern, yet traditional with the indian culture, we are looking for colors that match our logo. The logo is a design of the building with the name of the restaurant. for more information on the restaurant go to www.saffronlanterncourt.example

Industry/Entity Type

Indian Restaurant

Contact Information for Business Card

we are looking for somthing thats modern, yet traditional with the indian culture, we are looking for colors that match our logo. The logo is a design of the building with the name of the restaurant. for more information on the restaurant go to www.saffronlanterncourt.example

Requirements
Must have
• The logo that is attached,
• Name: Harvinder Oberoi,
• address of the restaurant: 7328 West Larkspur Rd, Phoenix, Arizona, 85213
• Phone: (602) 555-0147
• Fax: (602) 555-0193
• Restaurant Catering Banquet
• Website: www.SaffronLanternCourt.example
Nice to have
• wanted to get something that goes with the theme of the restaurant, which is traditional but also keep a very professional and modern touch

```html
<!DOCTYPE html>
<html lang="en">
<head>
<meta charset="utf-8">
<title>Saffron Lantern Court — Business Card</title>
<link rel="stylesheet" href="https://fonts.googleapis.com/css2?family=Lato:wght@400;700&family=Pinyon+Script&display=swap">
<style>
  :root {
    --page-bg: #ececec;
    --card-dark: #1b1b1b;
    --mark-grey: #8a8a8a;
    --since-grey: #5a5a5a;
    --cream-light: #f1ece1;
    --cream-mid: #e2d9c6;
    --cream-deep: #d6cbb3;
    --accent-red: #a3161f;
    --text-grey: #555555;
    --title-grey: #4a4a4a;
    --faint-grey: rgba(110, 110, 110, 0.55);
  }
  * { box-sizing: border-box; margin: 0; padding: 0; }
  html, body {
    width: 1200px;
    height: 586px;
    overflow: hidden;
    background: var(--page-bg);
    font-family: "Lato", sans-serif;
  }
  .stage { position: relative; width: 1200px; height: 586px; }
  .card {
    position: absolute;
    top: 129px;
    width: 501px;
    height: 301px;
    overflow: hidden;
  }
  .card-front { left: 65px; background: var(--card-dark); }
  .brand-lockup {
    position: absolute;
    left: 0; right: 0;
    top: 100px;
    text-align: center;
    color: var(--mark-grey);
    font-weight: 700;
    font-size: 40px;
    line-height: 46px;
    letter-spacing: 3px;
    text-transform: uppercase;
  }
  .since {
    position: absolute;
    left: 0; right: 0;
    top: 252px;
    text-align: center;
    color: var(--since-grey);
    font-size: 9px;
    font-weight: 700;
    letter-spacing: 3px;
  }
  .card-back { left: 608px; }
  .damask-field {
    position: absolute;
    inset: 0;
    background: radial-gradient(ellipse at 50% 40%, var(--cream-light) 0%, var(--cream-mid) 65%, var(--cream-deep) 100%);
  }
  .holder-name {
    position: absolute;
    left: 0; right: 0;
    top: 30px;
    text-align: center;
    font-family: "Pinyon Script", cursive;
    font-weight: 400;
    color: var(--accent-red);
    font-size: 38px;
    line-height: 48px;
  }
  .holder-title {
    position: absolute;
    left: 0; right: 0;
    top: 82px;
    text-align: center;
    font-size: 11px;
    letter-spacing: 2px;
    color: var(--title-grey);
  }
  .faint-brand {
    position: absolute;
    left: 0; right: 0;
    top: 148px;
    text-align: center;
    font-size: 26px;
    font-weight: 700;
    letter-spacing: 4px;
    text-transform: uppercase;
    color: var(--faint-grey);
  }
  .services {
    position: absolute;
    left: 0; right: 0;
    top: 196px;
    text-align: center;
    font-size: 10px;
    letter-spacing: 3px;
    text-transform: uppercase;
    color: var(--title-grey);
  }
  .contact-row {
    position: absolute;
    left: 0; right: 0;
    top: 248px;
    display: flex;
    justify-content: center;
    gap: 22px;
    font-size: 12px;
    color: var(--text-grey);
  }
  .contact-item { display: flex; align-items: center; gap: 4px; white-space: nowrap; }
  .contact-icon { width: 12px; height: 11px; fill: var(--accent-red); }
  .address {
    position: absolute;
    left: 0; right: 0;
    top: 274px;
    text-align: center;
    font-size: 12px;
    font-weight: 700;
    color: var(--accent-red);
  }
</style>
</head>
<body>
<main class="stage">
  <section class="card card-front">
    <div class="brand-lockup">Saffron<br>Lantern<br>Court</div>
    <div class="since">SINCE 1985</div>
  </section>

  <section class="card card-back">
    <div class="damask-field" role="img" aria-label="Cream damask scroll pattern background"></div>
    <h1 class="holder-name">Harvinder Oberoi</h1>
    <p class="holder-title">Marketing Director</p>
    <p class="faint-brand">Saffron Lantern Court</p>
    <p class="services">Restaurant · Catering · Banquet</p>
    <div class="contact-row">
      <span class="contact-item">
        <svg class="contact-icon" viewBox="0 0 12 11" aria-hidden="true"><path d="M1 3 Q6 -1 11 3 L9.5 4.5 L8 3.5 L8 2.5 Q6 1.8 4 2.5 L4 3.5 L2.5 4.5 Z"/><rect x="2.5" y="5" width="7" height="5.5" rx="1"/></svg>
        (602) 555-0147
      </span>
      <span class="contact-item">
        <svg class="contact-icon" viewBox="0 0 12 11" aria-hidden="true"><rect x="3" y="0.5" width="6" height="3"/><rect x="0.5" y="3.5" width="11" height="5" rx="1"/><rect x="3" y="7" width="6" height="3.5" fill="#fff"/></svg>
        (602) 555-0193
      </span>
      <span class="contact-item">
        <svg class="contact-icon" viewBox="0 0 12 12" aria-hidden="true"><circle cx="6" cy="6" r="5.3" fill="none" stroke="#a3161f" stroke-width="1.2"/><ellipse cx="6" cy="6" rx="2.3" ry="5.3" fill="none" stroke="#a3161f" stroke-width="1"/><path d="M0.8 6 H11.2" stroke="#a3161f" stroke-width="1"/></svg>
        www.SaffronLanternCourt.example
      </span>
    </div>
    <p class="address">7328 West Larkspur Rd, Phoenix Arizona, 85213</p>
  </section>
</main>
</body>
</html>
```